Fernwick

We require a professional design for a Cosmetic Surgery college. We have just submitted the request for our new logo which will be used on this card. We are the leaders in our field of education in Australia and this should be reflected in the quality of the card. People want to come and study with us because we are so outstanding in the field. Studying with us provides credibility, quality and courage.
Updates

Project Deadline Extended
Reason: Require updated logo to be used in design

Target Market(s)

25 - 40 year old professional women primarily from a medical background wanting to continue study in the cosmetic medical field, western speaking countries. The course average cost is 17k AU for 16 weeks.

Industry/Entity Type

Education

Requirements
Must have
• Must us the logo that is currently under design by this company.
Nice to have
• A medical twist very subtle would be nice possilbly rod of Asclepius.
Should not have
• Should not look old, we are dealing with modern medical concepts.
The logo that is being redesigned 3d silver, the attached logo is the old one.

```html
<!DOCTYPE html>
<html lang="en">
<head>
<meta charset="utf-8">
<title>Fernwick – Business Card</title>
<link rel="stylesheet" href="https://fonts.googleapis.com/css2?family=Noto+Serif:wght@400;700&display=swap">
<style>
  :root {
    --page-bg: #e9e7e4;
    --card-dark: #252324;
    --card-dark-edge: #1a1819;
    --silver: #c8c8ca;
    --silver-deep: #8e8e92;
    --band-white: #ffffff;
    --band-soft: #e4e4e4;
    --ink-dark: #1f1d1e;
    --text-light: #f4f4f4;
  }
  * { box-sizing: border-box; margin: 0; padding: 0; }
  html, body { width: 1200px; height: 1200px; overflow: hidden; }
  body {
    background: var(--page-bg);
    font-family: "Noto Serif", Georgia, serif;
    position: relative;
  }
  .card {
    position: absolute;
    left: 150px;
    width: 900px;
    height: 500px;
    border-radius: 6px;
    background: radial-gradient(ellipse at 40% 30%, var(--card-dark) 0%, var(--card-dark-edge) 100%);
    box-shadow: 0 10px 30px rgba(0,0,0,0.25);
    overflow: hidden;
  }
  .card--front { top: 60px; }
  .card--back { top: 640px; }

  .brand {
    position: absolute;
    display: flex;
    align-items: center;
    color: var(--silver);
    font-weight: 700;
  }
  .brand__dot {
    border-radius: 50%;
    background: var(--silver-deep);
    flex: none;
  }
  .card--front .brand { left: 70px; top: 70px; gap: 28px; font-size: 64px; letter-spacing: 3px; }
  .card--front .brand__dot { width: 110px; height: 110px; }
  .card--back .brand { left: 110px; top: 150px; gap: 40px; font-size: 78px; letter-spacing: 4px; }
  .card--back .brand__dot { width: 200px; height: 200px; }

  .role-band {
    position: absolute;
    left: 0; right: 0;
    top: 245px;
    height: 62px;
    display: flex;
  }
  .role-band__name {
    width: 330px;
    background: var(--band-soft);
    color: var(--ink-dark);
    font-size: 30px;
    display: flex;
    align-items: center;
    padding-left: 120px;
  }
  .role-band__chevron { width: 34px; height: 62px; flex: none; background: var(--band-white); }
  .role-band__title {
    flex: 1;
    background: var(--band-white);
    color: var(--ink-dark);
    font-size: 30px;
    display: flex;
    align-items: center;
    padding-left: 40px;
  }

  .contact {
    position: absolute;
    top: 335px;
    display: flex;
    flex-direction: column;
    align-items: center;
    color: var(--text-light);
    font-size: 25px;
    line-height: 1.3;
    text-align: center;
  }
  .contact__icon { width: 30px; height: 30px; margin-bottom: 12px; fill: var(--text-light); }
  .contact--address { left: 110px; width: 160px; }
  .contact--phone { left: 330px; width: 280px; }
  .contact--web { left: 620px; width: 260px; }
</style>
</head>
<body>

<section class="card card--front">
  <div class="brand"><span class="brand__dot"></span><span class="brand__name">FERNWICK</span></div>

  <div class="role-band">
    <div class="role-band__name">Name</div>
    <svg class="role-band__chevron" viewBox="0 0 34 62" aria-hidden="true">
      <rect width="34" height="62" fill="var(--band-white)"/>
      <polygon points="0,0 20,31 0,62" fill="var(--band-soft)"/>
      <polyline points="2,0 22,31 2,62" fill="none" stroke="var(--ink-dark)" stroke-width="3"/>
    </svg>
    <div class="role-band__title">Manager</div>
  </div>

  <div class="contact contact--address">
    <svg class="contact__icon" viewBox="0 0 24 24" aria-hidden="true">
      <path d="M12 1C7.6 1 4.5 4.2 4.5 8.4 4.5 14 12 23 12 23s7.5-9 7.5-14.6C19.5 4.2 16.4 1 12 1zm0 10.5a3 3 0 1 1 0-6 3 3 0 0 1 0 6z"/>
    </svg>
    <span>23, Avery</span>
    <span>AU</span>
  </div>

  <div class="contact contact--phone">
    <svg class="contact__icon" viewBox="0 0 24 24" aria-hidden="true">
      <path d="M6.6 10.8a15.1 15.1 0 0 0 6.6 6.6l2.2-2.2c.3-.3.7-.4 1-.2 1.1.4 2.3.6 3.6.6.6 0 1 .4 1 1V20c0 .6-.4 1-1 1A17 17 0 0 1 3 4c0-.6.4-1 1-1h3.5c.6 0 1 .4 1 1 0 1.3.2 2.5.6 3.6.1.3 0 .7-.2 1z"/>
    </svg>
    <span>+61 3 9555 0142</span>
    <span>+61 3 9555 0142</span>
  </div>

  <div class="contact contact--web">
    <svg class="contact__icon" viewBox="0 0 24 24" aria-hidden="true">
      <g fill="none" stroke="var(--text-light)" stroke-width="1.8">
        <circle cx="12" cy="12" r="10"/>
        <ellipse cx="12" cy="12" rx="4.5" ry="10"/>
        <line x1="2" y1="12" x2="22" y2="12"/>
        <path d="M4 6.5h16M4 17.5h16"/>
      </g>
    </svg>
    <span>hello@fernwick.edu</span>
    <span>www.fernwick.edu</span>
  </div>
</section>

<section class="card card--back">
  <div class="brand"><span class="brand__dot"></span><span class="brand__name">FERNWICK</span></div>
</section>

</body>
</html>
```